One of Australia's fastest growing Financial Company looking for an updated business card design!

Meridale Holdings Australia is looking for an updated design for our business cards. We would like to keep up our professional appearances and have get new exciting design that fits our company.

The Meridale aim is to facilitate and assist clients in every financial requirement that may arise in financial areas.

We would to see the design to use colour blue and we like the clouds in the background. We have attached two designs we have use before but we need something with more professional and easy to read design.

We would like the website in the back of the card; the employees name more central and stands out; only a postal address; a list of all our locations along the bottom (Sydney, Melbourne, Brisbane, Singapore)

Looking forward to seeing the designs come in!

Target Market(s)

Other Industry Professionals
Middle Class Families

Industry/Entity Type

Finance

Contact Information for Business Card

Name; Company Role; Office Number; Mobile Number; Email Address; Website; Postal Address; Locations

Font styles to use
Serif
Sans Serif

Colors
0492cd
33a6d7
85cae6
85acd3
3176b5
0455a3
cee9f5
d5e2ee

Requirements
Must have
• Name; Company Role; Office Number; Mobile Number; Email Address; Website; Postal Address; Locations
Nice to have
• The colour blue, clouds on the background

```html
<!DOCTYPE html>
<html lang="en">
<head>
<meta charset="utf-8">
<title>Meridale Business Card – Design Two</title>
<link href="https://fonts.googleapis.com/css2?family=PT+Sans:wght@400;700&display=swap" rel="stylesheet">
<style>
  :root {
    --board: #e1e2e4;
    --title-grey: #6d6e70;
    --white: #ffffff;
    --brand-blue: #1a8fd6;
    --role-blue: #1d4fa3;
    --sky-light: #a9cbe8;
    --sky-mid: #3d86c4;
    --sky-deep: #0d4c8a;
    --rule: rgba(255,255,255,0.55);
    --edge: #c9ccd0;
  }
  * { box-sizing: border-box; margin: 0; padding: 0; }
  html, body {
    width: 1200px; height: 1200px; overflow: hidden;
    background: var(--board);
    font-family: "PT Sans", sans-serif;
  }
  .board { position: relative; width: 1200px; height: 1200px; }
  .board-title {
    position: absolute; left: 99px; top: 84px;
    font-size: 29px; font-weight: 700; color: var(--title-grey);
    letter-spacing: -0.3px;
  }
  .card {
    position: absolute; overflow: hidden;
    border-radius: 22px; border: 1px solid var(--edge);
    background: var(--white);
  }
  .sky {
    position: absolute; left: 0; right: 0; bottom: 0;
    background:
      radial-gradient(ellipse 45% 60% at 18% 45%, rgba(255,255,255,0.75), rgba(255,255,255,0) 70%),
      radial-gradient(ellipse 30% 50% at 88% 10%, rgba(255,255,255,0.45), rgba(255,255,255,0) 70%),
      linear-gradient(135deg, var(--sky-light) 0%, var(--sky-mid) 45%, var(--sky-deep) 100%);
  }
  /* Front */
  .card-front { left: 99px; top: 208px; width: 655px; height: 362px; }
  .card-front .sky { top: 82px; }
  .brand {
    position: absolute; display: flex; align-items: center; gap: 12px;
    font-size: 56px; font-weight: 400; color: var(--brand-blue); line-height: 1;
  }
  .brand-dot { width: 36px; height: 36px; border-radius: 50%; background: var(--brand-blue); }
  .card-front .brand { right: 42px; top: 14px; }
  .person {
    position: absolute; left: 330px; top: 112px; width: 300px; text-align: center;
  }
  .person-name { font-size: 30px; color: var(--white); line-height: 1.1; }
  .person-role { font-size: 19px; color: var(--role-blue); margin-top: 2px; }
  .contact {
    position: absolute; left: 335px; top: 202px; color: var(--white);
  }
  .contact-company { font-size: 18px; font-weight: 700; margin-bottom: 2px; }
  .contact-line { font-size: 14.5px; line-height: 19.5px; }
  .contact-rule {
    position: absolute; left: 331px; right: 5px; top: 290px;
    height: 1px; background: var(--rule);
  }
  .locations {
    position: absolute; right: 36px; top: 316px;
    font-size: 19px; color: var(--white);
  }
  /* Back */
  .card-back { left: 445px; top: 638px; width: 647px; height: 359px; }
  .card-back .sky { top: 0; }
  .brand-box {
    position: absolute; left: 245px; top: 182px; width: 300px; height: 92px;
    background: var(--white); border-radius: 18px;
  }
  .card-back .brand { left: 272px; top: 200px; }
  .website {
    position: absolute; right: 26px; top: 296px;
    font-size: 24px; color: var(--white); letter-spacing: 0.3px;
  }
</style>
</head>
<body>
<main class="board">
  <h1 class="board-title">BUISNESS CARD DESIGN TWO</h1>

  <section class="card card-front">
    <div class="brand"><span class="brand-dot"></span>Meridale</div>
    <div class="sky" role="img" aria-label="Photograph of blue sky with white clouds and sun rays"></div>
    <div class="person">
      <p class="person-name">Hannah Brooks</p>
      <p class="person-role">Investment Consultant</p>
    </div>
    <div class="contact">
      <p class="contact-company">Meridale Holdings Australia Pty Ltd</p>
      <p class="contact-line">Off No: (02) 6500 1234 Mobile No: 0400 555 018</p>
      <p class="contact-line">Email : info@meridaleholdings.com.au</p>
      <p class="contact-line">Kingsford Post Shop PO BOX 1180</p>
    </div>
    <div class="contact-rule"></div>
    <p class="locations">Sydney, Melbourne, Brisbane, Singapore</p>
  </section>

  <section class="card card-back">
    <div class="sky" role="img" aria-label="Photograph of blue sky with white clouds and sun rays"></div>
    <div class="brand-box"></div>
    <div class="brand"><span class="brand-dot"></span>Meridale</div>
    <p class="website">www.meridaleholdings.com.au</p>
  </section>
</main>
</body>
</html>
```